Infographic for Commercial Painting and Flooring Company

We need an Infographic that shows a compelling argument for signing on with Brenvoria for a maintenance contract vs a project. The infographic should be easily understood visually so sell the story we have provided. 1) What does the quick view give me? 2) Am I interested in this? 3) Does this bring me any value? 4) Is this “everything I have seen before or something new and different”? Included here is a word document called Maintenance vs Project Notes with the written content and instructions, a logo, and two other marketing pieces they currently use so you can see how their brand is being used. Colors should be on brand. I'd like to get this done ASAP if possible. We do not want this piece to look busy.

I added two images called Sample 1 and Sample 2 to portray the types of infographics we like. Simple and clear. Love the watch with the pie chart built in....a smaller version of that would be great for us based on the notes document I provided.

Target Market(s)

Facilities Manufacturers and owners of manufacturing facilities

Font styles to use
Sans Serif

Colors

Designer to choose colors to be used in the design.

Requirements
Must have
• Simple, clean, tell a clear story
Nice to have
• Iconography, pie chart, Men in hard hat
Should not have
• Too many colors. Stick with the brand colors and maybe a few others. Don't want it too look to busy.

```html
<!DOCTYPE html>
<html lang="en">
<head>
<meta charset="utf-8">
<title>Brenvoria – Maintenance vs Project Infographic</title>
<link href="https://fonts.googleapis.com/css2?family=Roboto:ital,wght@0,300;0,400;0,700;1,400&display=swap" rel="stylesheet">
<style>
  :root {
    --navy: #0d3b6e;
    --olive: #8c8c14;
    --cream: #f5f3e6;
    --band-light: #ecead2;
    --band-dark: #b7b68a;
    --white: #ffffff;
    --canvas: #ffffff;
  }
  * { margin: 0; padding: 0; box-sizing: border-box; }
  html, body { width: 1200px; height: 1200px; overflow: hidden; background: var(--canvas); }
  body { font-family: "Roboto", Arial, sans-serif; color: var(--navy); position: relative; }
  .page { position: absolute; left: 216px; top: 61px; width: 776px; height: 1085px; background: var(--cream);
    overflow: hidden; box-shadow: 0 0 28px rgba(0,0,0,.18); }
  .abs { position: absolute; }

  .hero-band { left: 0; top: 0; }
  .brand { left: 28px; top: 44px; display: flex; align-items: center; gap: 8px; }
  .brand-mark { width: 20px; height: 20px; background: var(--olive); }
  .brand-name { font-weight: 700; font-size: 25px; line-height: 28px; color: var(--navy); }

  .headline { left: 90px; top: 99px; font-weight: 700; font-size: 29px; line-height: 31px; white-space: nowrap; }
  .intro { left: 90px; top: 203px; font-weight: 300; font-size: 14px; line-height: 16.6px; width: 320px; }
  .worker { left: 528px; top: 8px; width: 155px; height: 298px; border-radius: 78px 78px 10px 10px;
    background: linear-gradient(180deg, #e7a43a 0%, #1f4b8a 33%, #1f4b8a 60%, #222 100%); opacity: .85; }

  .rule { background: var(--olive); height: 3px; }
  .rule-top { left: 31px; top: 310px; width: 714px; }

  .section-title { left: 0; width: 776px; top: 329px; text-align: center; font-weight: 700; font-size: 19.5px; line-height: 22px; }

  .pie-wrap { width: 107px; height: 107px; }
  .pie { width: 107px; height: 107px; display: block; }
  .pie-value { position: absolute; transform: translate(-50%, -50%); color: var(--white); font-weight: 700;
    font-size: 9.5px; line-height: 10.5px; text-align: center; white-space: nowrap; }
  .pie-value span { display: block; font-size: 10.5px; line-height: 11px; }
  .step { width: 122px; text-align: center; font-weight: 300; font-size: 10px; line-height: 12px; }
  .step::before { content: ""; display: block; height: 1.5px; background: var(--navy); margin-bottom: 6px; }

  .stat-big { left: 98px; top: 721px; font-weight: 700; font-size: 24px; line-height: 28px; white-space: nowrap; }
  .stat-big small { font-size: 14px; }
  .stat-note { left: 101px; top: 753px; font-weight: 300; font-size: 10px; line-height: 16px; white-space: nowrap; }
  .stat-note b { font-weight: 700; }
  .stat-note .pct { font-size: 15px; font-weight: 700; }
  .stat-once { left: 98px; top: 782px; font-weight: 700; font-size: 25px; line-height: 30px; white-space: nowrap; }
  .stat-once small { font-size: 14px; }
  .stat-once-note { left: 98px; top: 817px; font-weight: 300; font-size: 10px; line-height: 14px; white-space: nowrap; }
  .stat-once-note b { font-weight: 700; }

  .rule-partner { left: 404px; top: 714px; width: 341px; }
  .partner-title { left: 404px; top: 725px; font-weight: 700; font-size: 19.5px; line-height: 24px; white-space: nowrap; }
  .partner-box { left: 404px; top: 780px; width: 341px; height: 195px; background: var(--olive); }
  .values { left: 16px; top: 29px; width: 84px; }
  .values li { list-style: none; color: var(--white); font-weight: 700; font-size: 13.5px; line-height: 23.5px; white-space: nowrap; }
  .values-rule { height: 1.5px; background: var(--white); margin: 3px 0 5px; width: 82px; }
  .values-tag { color: var(--white); font-style: italic; font-size: 12px; line-height: 11px; white-space: nowrap; }
  .benefits { left: 109px; top: 4px; width: 223px; }
  .benefits li { list-style: none; font-weight: 300; font-size: 9px; line-height: 16px; height: 16px; margin-bottom: 2px;
    padding: 0 6px; color: var(--white); white-space: nowrap; }
  .benefits li.boxed { background: var(--white); color: var(--olive); }
  .benefits li.tall { height: 28px; line-height: 11px; padding-top: 3px; white-space: normal; }

  .focus-wheel { left: 76px; top: 905px; }
  .focus-text { width: 130px; text-align: center; color: var(--white); font-weight: 300; font-size: 10px; line-height: 11.7px; }
</style>
</head>
<body>
<main class="page">
  <svg class="abs hero-band" width="776" height="320" viewBox="0 0 776 320" aria-hidden="true">
    <defs>
      <linearGradient id="band" x1="0" y1="1" x2="1" y2="0">
        <stop offset="0" stop-color="var(--band-light)"/>
        <stop offset="1" stop-color="var(--band-dark)"/>
      </linearGradient>
    </defs>
    <path d="M0 301 C30 270 90 276 230 279 C380 282 470 240 530 180 C580 130 640 140 690 110 C715 90 720 40 720 0 L0 0 Z" fill="url(#band)"/>
  </svg>

  <div class="abs brand"><span class="brand-mark"></span><span class="brand-name">Brenvoria</span></div>

  <h1 class="abs headline">Imagine What You Could Do<br>with An Extra 30%<br>More Time Each Year?</h1>
  <p class="abs intro">Time that you wouldn't need to spend on-boarding a new company every time you have a project or facility upgrade.</p>

  <div class="abs worker" role="img" aria-label="Illustration of a thoughtful worker in a hard hat with a question-mark thought bubble"></div>

  <div class="abs rule rule-top"></div>
  <h2 class="abs section-title">It Takes 30+ Hours to Source<br>and Onboard the Most QualifiedVendor...YIKES!</h2>

  <!-- Row 1 -->
  <div class="abs pie-wrap" style="left:103px;top:398px">
    <svg class="pie" viewBox="0 0 120 120"><circle cx="60" cy="60" r="59" fill="var(--olive)"/><path d="M60 60 L60 1 A59 59 0 0 1 111.1 89.5 Z" fill="var(--navy)"/></svg>
    <div class="pie-value" style="left:80px;top:41px">4<span>HOURS</span></div>
  </div>
  <div class="abs step" style="left:95px;top:516px">Source Vendors &amp; Bidders</div>

  <div class="abs pie-wrap" style="left:257px;top:398px">
    <svg class="pie" viewBox="0 0 120 120"><circle cx="60" cy="60" r="59" fill="var(--olive)"/><path d="M60 60 L60 1 A59 59 0 1 1 30.5 111.1 Z" fill="var(--navy)"/></svg>
    <div class="pie-value" style="left:77px;top:67px">7<span>HOURS</span></div>
  </div>
  <div class="abs step" style="left:266px;top:516px">Schedule and Completing a Walkthrough</div>

  <div class="abs pie-wrap" style="left:411px;top:398px">
    <svg class="pie" viewBox="0 0 120 120"><circle cx="60" cy="60" r="59" fill="var(--olive)"/><path d="M60 60 L60 1 A59 59 0 0 1 119 60 Z" fill="var(--navy)"/></svg>
    <div class="pie-value" style="left:77px;top:33px">3<span>HOURS</span></div>
  </div>
  <div class="abs step" style="left:404px;top:516px">Reviewing Estimates</div>

  <div class="abs pie-wrap" style="left:566px;top:398px">
    <svg class="pie" viewBox="0 0 120 120"><circle cx="60" cy="60" r="59" fill="var(--olive)"/><path d="M60 60 L60 1 A59 59 0 0 1 111.1 89.5 Z" fill="var(--navy)"/></svg>
    <div class="pie-value" style="left:79px;top:38px">4<span>HOURS</span></div>
  </div>
  <div class="abs step" style="left:558px;top:516px">Phone calls to clarify scope and any big revisions</div>

  <!-- Row 2 -->
  <div class="abs pie-wrap" style="left:103px;top:555px">
    <svg class="pie" viewBox="0 0 120 120"><circle cx="60" cy="60" r="59" fill="var(--olive)"/><path d="M60 60 L60 1 A59 59 0 0 1 111.1 30.5 Z" fill="var(--navy)"/></svg>
    <div class="pie-value" style="left:73px;top:21px">2<span>HOURS</span></div>
  </div>
  <div class="abs step" style="left:97px;top:672px">Present to Decision Maker &amp; Financing Approval</div>

  <div class="abs pie-wrap" style="left:257px;top:555px">
    <svg class="pie" viewBox="0 0 120 120"><circle cx="60" cy="60" r="59" fill="var(--olive)"/><path d="M60 60 L60 1 A59 59 0 0 1 111.1 89.5 Z" fill="var(--navy)"/></svg>
    <div class="pie-value" style="left:80px;top:41px">4<span>HOURS</span></div>
  </div>
  <div class="abs step" style="left:250px;top:672px">Negotiations with Vendor</div>

  <div class="abs pie-wrap" style="left:411px;top:555px">
    <svg class="pie" viewBox="0 0 120 120"><circle cx="60" cy="60" r="59" fill="var(--olive)"/><path d="M60 60 L60 1 A59 59 0 0 1 119 60 Z" fill="var(--navy)"/></svg>
    <div class="pie-value" style="left:77px;top:33px">3<span>HOURS</span></div>
  </div>
  <div class="abs step" style="left:404px;top:672px">Awarding &amp; Purchasing</div>

  <div class="abs pie-wrap" style="left:566px;top:555px">
    <svg class="pie" viewBox="0 0 120 120"><circle cx="60" cy="60" r="59" fill="var(--olive)"/><path d="M60 60 L60 1 A59 59 0 0 1 119 60 Z" fill="var(--navy)"/></svg>
    <div class="pie-value" style="left:77px;top:33px">3<span>HOURS</span></div>
  </div>
  <div class="abs step" style="left:558px;top:672px">Completing On-Boarding Paperwork</div>

  <!-- Stats -->
  <div class="abs stat-big">20<small>Projects</small> = 600<small>Hours</small></div>
  <div class="abs stat-note">or <span class="pct">25%</span> of Your Time Per Year....<b>OUGGH!</b></div>
  <div class="abs stat-once">On-Boarding <small>Once</small> = 1.5 %</div>
  <div class="abs stat-once-note">of Your Time for the entire year...<b>FOR REAL!</b></div>

  <!-- Partner -->
  <div class="abs rule rule-partner"></div>
  <h2 class="abs partner-title">You'll Have A Trusted Partner<br>Who Provides...</h2>
  <section class="abs partner-box">
    <div class="abs values">
      <ul>
        <li>Consistency</li>
        <li>Predictability</li>
        <li>Reliability</li>
      </ul>
      <div class="values-rule"></div>
      <p class="values-tag">Aligned with<br>Your Needs</p>
    </div>
    <ul class="abs benefits">
      <li class="boxed">Safety Is Our #1 Objective</li>
      <li>Adapting to all ofYour Scheduling Requirements</li>
      <li class="boxed">A Single Point of Communication</li>
      <li>Integration w/ your Work Order Process &amp; Project</li>
      <li class="boxed">Tracking</li>
      <li class="tall">A Dedicated Field Team,who Understands<br>the Ins and Outs of Your Facility</li>
      <li class="boxed">Rapid Response Time</li>
      <li>All Tasks and Jobs (Big or Small) Equally Prioritized</li>
      <li class="boxed">Customized Billing and Future Budget Building</li>
      <li>Visual Facility Mapping</li>
    </ul>
  </section>

  <!-- Focus wheel -->
  <svg class="abs focus-wheel" width="360" height="180" viewBox="0 0 360 180" aria-hidden="true">
    <path d="M0 180 A180 180 0 0 1 360 180 Z" fill="var(--navy)"/>
    <line x1="180" y1="180" x2="92" y2="24" stroke="var(--white)" stroke-width="2.5"/>
    <line x1="180" y1="180" x2="268" y2="24" stroke="var(--white)" stroke-width="2.5"/>
    <g transform="translate(180 118)">
      <polygon points="-6,-21 6,-21 12,15 -12,15" fill="var(--olive)"/>
      <polygon points="-8,-8 8,-8 9.5,-1 -9.5,-1" fill="var(--white)"/>
      <polygon points="-10.5,4 10.5,4 12,10 -12,10" fill="var(--white)"/>
      <rect x="-15" y="15" width="30" height="3" fill="var(--olive)"/>
    </g>
    <g transform="translate(134 150) rotate(-30)">
      <rect x="-11" y="-18" width="22" height="36" rx="3" fill="var(--olive)"/>
      <rect x="-8" y="-14" width="16" height="26" rx="1" fill="var(--white)"/>
      <circle cx="0" cy="15.5" r="1.3" fill="var(--white)"/>
    </g>
    <g fill="var(--olive)">
      <circle cx="224" cy="148" r="10"/>
      <circle cx="224" cy="148" r="12.5" fill="none" stroke="var(--olive)" stroke-width="4" stroke-dasharray="3.2 2.8"/>
      <circle cx="224" cy="148" r="3.5" fill="var(--white)"/>
      <circle cx="244" cy="163" r="7"/>
      <circle cx="244" cy="163" r="9" fill="none" stroke="var(--olive)" stroke-width="3" stroke-dasharray="2.5 2.4"/>
      <circle cx="244" cy="163" r="2.4" fill="var(--white)"/>
    </g>
  </svg>
  <p class="abs focus-text" style="left:191px;top:939px">Focus on<br>Safety to ensure<br>it is a priority</p>
  <p class="abs focus-text" style="left:83px;top:998px">Focus on<br>Communication<br>with Your Team<br>and Customers</p>
  <p class="abs focus-text" style="left:294px;top:998px">Focus on<br>Productivity to ensure<br>you meet all of your<br>business unit's needs</p>
</main>
</body>
</html>
```